High End Business Card Design for Flooring Store

Looking for a new card design for our hardwood flooring company. We have no print budget for these and are open to cards made from wood, metal, cardstock with embossed print ... or any combination of these. No plastic.

We sell luxury products and I want the cards to reflect our image of quality and class.

Our contact information as such;
Employee Name
418 Colbrook Blvd.
Lorrance, NS
K9R-3M5
(555) 214-3968
Employee email @velkaflooring.com

Target Market(s)

Home Builders

Contact Information for Business Card

Emnployee name, business contact information

```html
<!DOCTYPE html>
<html lang="en">
<head>
<meta charset="utf-8">
<title>Velka Flooring – Business Card</title>
<link rel="stylesheet" href="https://fonts.googleapis.com/css2?family=Source+Sans+3:ital,wght@0,600;1,600;1,700&family=Montserrat:wght@400;500&display=swap">
<style>
  :root {
    --backdrop: #e9e9e9;
    --card-white: #ffffff;
    --brand-red: #922a25;
    --accent-gold: #e8b22a;
    --ink: #1c1c1c;
    --frame-grey: #5e5e5e;
    --tagline-grey: #8e8e8e;
    --icon-grey: #7a7a7a;
  }
  * { margin: 0; padding: 0; box-sizing: border-box; }
  html, body { width: 1200px; height: 1200px; overflow: hidden; }
  body { background: var(--backdrop); position: relative; font-family: "Source Sans 3", sans-serif; color: var(--ink); }

  .card { position: absolute; left: 237px; width: 730px; height: 415px; border-radius: 40px; overflow: hidden; }
  .card--front { top: 157px; background: var(--card-white); }
  .card--back { top: 650px; background: var(--brand-red); }

  .frame { position: absolute; left: 0; top: 0; width: 730px; height: 415px; }

  .identity { position: absolute; right: calc(730px - 349px); top: 164px; text-align: right; }
  .identity__name { font-size: 31px; font-weight: 700; font-style: italic; color: var(--brand-red); line-height: 1; letter-spacing: 0.2px; }
  .identity__role { font-size: 12.5px; font-weight: 600; font-style: italic; margin-top: 9px; }

  .divider { position: absolute; left: 369px; top: 124px; width: 1.5px; height: 133px; background: var(--frame-grey); }

  .contacts { position: absolute; left: 383px; top: 143px; list-style: none; }
  .contacts__item { display: flex; align-items: center; height: 27px; font-size: 17px; font-weight: 600; }
  .contacts__icon { width: 21px; height: 21px; margin-right: 9px; flex: none; }

  .address { position: absolute; left: 0; width: 730px; top: 346px; text-align: center; font-size: 17px; font-weight: 600; line-height: 22px; }

  .brand { position: absolute; left: 0; width: 730px; top: 108px; display: flex; justify-content: center; align-items: center; gap: 18px; }
  .brand__square { width: 58px; height: 58px; background: var(--accent-gold); }
  .brand__name { font-family: "Montserrat", sans-serif; font-weight: 400; font-size: 128px; line-height: 1; color: #ffffff; letter-spacing: -1px; }

  .tagline { position: absolute; left: 30px; width: 730px; top: 237px; text-align: center; font-family: "Montserrat", sans-serif; font-weight: 500; font-size: 31px; line-height: 35px; color: var(--tagline-grey); }
</style>
</head>
<body>

  <section class="card card--front" aria-label="Business card, contact side">
    <svg class="frame" viewBox="0 0 730 415" aria-hidden="true">
      <path d="M158 373 H62 A42 42 0 0 1 20 331 V57 A42 42 0 0 1 62 15 H668 A42 42 0 0 1 710 57 V331 A42 42 0 0 1 668 373 H585"
            fill="none" stroke="var(--frame-grey)" stroke-width="2"/>
    </svg>

    <div class="identity">
      <p class="identity__name">My Name</p>
      <p class="identity__role">Founder &amp; Director</p>
    </div>

    <span class="divider"></span>

    <ul class="contacts">
      <li class="contacts__item">
        <svg class="contacts__icon" viewBox="0 0 22 22" aria-hidden="true">
          <circle cx="11" cy="11" r="10" fill="none" stroke="var(--icon-grey)" stroke-width="1.2"/>
          <path d="M7.5 6.5 l2 0.3 0.6 2.3 -1.2 1 a7 7 0 0 0 3 3 l1-1.2 2.3 0.6 0.3 2 a1.5 1.5 0 0 1 -1.6 1.3 A8 8 0 0 1 6.2 8.1 1.5 1.5 0 0 1 7.5 6.5z" fill="var(--ink)"/>
        </svg>
        (555) 214-3968
      </li>
      <li class="contacts__item">
        <svg class="contacts__icon" viewBox="0 0 22 22" aria-hidden="true">
          <circle cx="11" cy="11" r="10" fill="none" stroke="var(--icon-grey)" stroke-width="1.2"/>
          <rect x="8" y="5.5" width="6" height="11" rx="1" fill="none" stroke="var(--ink)" stroke-width="1.2"/>
        </svg>
        (000) 000-0000
      </li>
      <li class="contacts__item">
        <svg class="contacts__icon" viewBox="0 0 22 22" aria-hidden="true">
          <circle cx="11" cy="11" r="10" fill="none" stroke="var(--icon-grey)" stroke-width="1.2"/>
          <rect x="6" y="7.5" width="10" height="7" rx="0.8" fill="var(--ink)"/>
          <path d="M6.3 7.8 L11 11.5 15.7 7.8" fill="none" stroke="#fff" stroke-width="0.9"/>
        </svg>
        email @velkaflooring.com
      </li>
      <li class="contacts__item">
        <svg class="contacts__icon" viewBox="0 0 22 22" aria-hidden="true">
          <circle cx="11" cy="11" r="10" fill="none" stroke="var(--icon-grey)" stroke-width="1.2"/>
          <circle cx="11" cy="11" r="5.5" fill="none" stroke="var(--ink)" stroke-width="1"/>
          <ellipse cx="11" cy="11" rx="2.4" ry="5.5" fill="none" stroke="var(--ink)" stroke-width="0.9"/>
          <path d="M5.5 11 H16.5" stroke="var(--ink)" stroke-width="0.9"/>
        </svg>
        www.velkaflooring.com
      </li>
    </ul>

    <p class="address">418 Colbrook Blvd.<br>Lorrance, NS, K9R-3M5</p>
  </section>

  <section class="card card--back" aria-label="Business card, brand side">
    <div class="brand">
      <span class="brand__square"></span>
      <span class="brand__name">Velka</span>
    </div>
    <p class="tagline">Planchers &amp; Escaliers<br>Flooring &amp; Stairs</p>
  </section>

</body>
</html>
```